Kelmora - Step into Wonder! Business Card

We are bringing an amazing new system of dance to Australia and need a nifty, eye-catching little card that we can give to everyone to get them to come to class.

It needs a bit of information about Kelmora, along with contact details and a space for us to write a note for people about the next class.

Target Market(s)

30+ people that enjoy dance and are interested in self-development, meeting people and getting more out of life.

Industry/Entity Type

Business

Requirements
Must have
• Double sided in colour

A beautiful, simple design that indicates movement and is modern, fresh and uplifting.

The attached Kelmora logo

Text for the front :

Kelmora - the Step into Wonder

Dance from your heart and feel your life open.

Regular classes in Sydney and Canberra with Mara Polden and Torsten Walby

Text for the back :

Kelmora ignites our vital spark for life and awakens our innate potential for pleasurable, joyful, heartfelt living through dance, music and authentic connection.

Torsten and Mara are committed to offering authentic, supportive and inspiring spaces for your growth through Kelmora.

Contact us on mara@kelmora.com.au - twbyrne@mailquest.net or 0491 570 284.

www.kelmora.com.au

Nice to have
• Some movement in the design

Use some of the photos attached in some form - could be faded, incorporated into design etc.

Creative use of the logo - integrating it within the design - e.g perhaps using it as the O in Kelmora,
Should not have
• Not a lot of black

```html
<!DOCTYPE html>
<html lang="en">
<head>
<meta charset="utf-8">
<title>Kelmora – Business Card</title>
<link rel="stylesheet" href="https://fonts.googleapis.com/css2?family=Oswald:wght@400;500&family=Pacifico&display=swap">
<style>
  :root {
    --stage-light: #f2f2f2;
    --stage-dark: #9a9a9a;
    --card-grey: #7b7b7b;
    --crimson: #cc0040;
    --crimson-deep: #a8002f;
    --white: #ffffff;
    --ink: #3a3a3a;
  }
  * { box-sizing: border-box; margin: 0; padding: 0; }
  html, body { width: 1200px; height: 900px; overflow: hidden; }
  body {
    position: relative;
    background: radial-gradient(ellipse 520px 420px at 600px 450px, var(--stage-light), var(--stage-dark));
    font-family: Arial, Helvetica, sans-serif;
    color: var(--white);
  }
  .card {
    position: absolute;
    left: 260px;
    width: 680px;
    height: 390px;
    overflow: hidden;
  }
  .card--front { top: 35px; background: var(--card-grey); }
  .card--back { top: 475px; background: var(--crimson); border: 1px solid var(--crimson-deep); }

  .photo { position: absolute; top: 0; height: 100%; }
  .card--front .photo {
    right: 0; width: 430px;
    background:
      linear-gradient(90deg, var(--card-grey) 0%, rgba(123,123,123,0.55) 22%, rgba(123,123,123,0) 45%),
      radial-gradient(ellipse 120px 160px at 330px 170px, #e6e2dc, transparent 70%),
      radial-gradient(ellipse 110px 140px at 170px 150px, #d8d2cc, transparent 70%),
      linear-gradient(180deg, #5a4a44 0%, #3e3632 55%, #6b625c 100%);
  }
  .card--back .photo {
    left: 0; width: 240px;
    background:
      linear-gradient(90deg, rgba(204,0,64,0) 0%, rgba(204,0,64,0.35) 55%, var(--crimson) 100%),
      radial-gradient(ellipse 60px 150px at 70px 220px, #e4e8ec, transparent 70%),
      linear-gradient(180deg, #b06a5c 0%, #8a4a44 50%, #5a3030 100%);
  }

  .brand-seal {
    position: absolute; left: 20px; top: 14px;
    width: 134px; height: 134px; border-radius: 50%;
    background: var(--white);
    display: flex; align-items: center; justify-content: center;
    font-family: Oswald, sans-serif; font-weight: 400; font-size: 26px; color: var(--ink);
  }
  .brand-name {
    position: absolute; left: 194px; top: 32px;
    font-family: Oswald, sans-serif; font-weight: 500; font-size: 82px; line-height: 1;
    letter-spacing: -1px;
  }
  .tagline-script {
    position: absolute; left: 170px; top: 140px; width: 340px;
    font-family: Pacifico, cursive; font-size: 30px; color: var(--crimson);
    text-align: center; white-space: nowrap;
  }
  .lead { position: absolute; left: 26px; top: 200px; font-size: 17px; }
  .classes {
    position: absolute; left: 0; width: 586px; top: 310px;
    text-align: center; font-size: 22px;
  }
  .teachers {
    position: absolute; left: 0; width: 586px; top: 345px;
    text-align: center; font-family: Pacifico, cursive; font-size: 19px; color: var(--crimson);
  }

  .about {
    position: absolute; left: 30px; width: 620px; top: 56px;
    text-align: center; font-size: 14px; line-height: 19px;
  }
  .about p + p { margin-top: 16px; }
  .contact {
    position: absolute; left: 200px; width: 280px; top: 180px;
    text-align: center; font-size: 22px; line-height: 28px;
  }
  .website {
    position: absolute; left: 200px; width: 280px; top: 354px;
    text-align: center; font-size: 15px;
  }
</style>
</head>
<body>
  <section class="card card--front">
    <div class="photo" role="img" aria-label="Photo of two smiling dancers holding hands during a class"></div>
    <div class="brand-seal">Kelmora</div>
    <h1 class="brand-name">Kelmora</h1>
    <p class="tagline-script">the Step into Wonder</p>
    <p class="lead">Dance from your heart and feel your life open</p>
    <p class="classes">Regular classes in Sydney and Canberra</p>
    <p class="teachers">with Mara Polden and Torsten Walby</p>
  </section>

  <section class="card card--back">
    <div class="photo" role="img" aria-label="Faded photo of two dancers moving together by a brick wall"></div>
    <div class="about">
      <p>Kelmora ignites our vital spark for life and awakens our innate potential for pleasurable,<br>joyful, heartfelt living through dance, music and authentic connection.</p>
      <p>Torsten and Mara are committed to offering authentic,<br>supportive and inspiring spaces for your growth through Kelmora.</p>
    </div>
    <div class="contact">
      <p>Contact us :</p>
      <p>mara@kelmora.com.au</p>
      <p>twbyrne@mailquest.net</p>
      <p>0491 570 284.</p>
    </div>
    <p class="website">www.kelmora.com.au</p>
  </section>
</body>
</html>
```